Flooring Billboard Highlighting Large In Stock Inventory

Looking to create a billboard that primarily highlights our logo but also calls out our large in stock inventory and has the city we are located in and phone number at the bottom. Looking for a professional looking design, that is simplistic yet informative.

Location: Maple Falls, WI, Near Exit 114

Phone: (715) 381-6094

Website: www.plankhavenstore.example

Products: Carpet, Hardwood, Laminate, Vinyl, Luxury Vinyl Plank & Window Treatments

Callouts:
-Free Estimates
-Wisconsin's In Stock Flooring Store
-Slogan: "Big city selection, small town service"

Target Market(s)

Home buyers, DIY'ers, Remoderls, designers

Industry/Entity Type

Flooring, Construction

Font styles to use
Serif

Requirements
Must have
• My logo, location, phone number and call out our large in stock inventory
Nice to have
• Call out the products we have and our slogan

```html
<!DOCTYPE html>
<html lang="en">
<head>
<meta charset="utf-8">
<title>Plank Haven Billboard</title>
<link rel="stylesheet" href="https://fonts.googleapis.com/css2?family=Bebas+Neue&family=Poppins:wght@400;500;600;700&display=swap">
<style>
  :root {
    --teal: #0d8a8f;
    --teal-dark: #0a6e72;
    --orange: #c2622a;
    --paper: #eeece7;
    --ink: #1d1d1d;
    --white: #ffffff;
    --stage: #e4e6e8;
  }
  * { margin: 0; padding: 0; box-sizing: border-box; }
  html, body { width: 1200px; height: 1157px; overflow: hidden; background: var(--stage); }
  .billboard {
    position: absolute; left: 0; top: 321px;
    width: 1200px; height: 514px;
    background: var(--paper);
    overflow: hidden;
    font-family: "Poppins", sans-serif;
  }
  .brand {
    position: absolute; left: 38px; top: 40px;
    display: flex; align-items: center; gap: 18px;
  }
  .brand-square { width: 86px; height: 86px; background: var(--teal); flex: none; }
  .brand-name {
    font-family: "Poppins", sans-serif; font-weight: 500;
    color: var(--teal); font-size: 84px; line-height: 0.98; letter-spacing: 1px;
  }
  .callouts { position: absolute; left: 32px; top: 270px; list-style: none; }
  .callouts li {
    display: flex; align-items: flex-start; gap: 16px;
    font-size: 29px; line-height: 37px; color: var(--ink); margin-bottom: 14px;
  }
  .callouts svg { flex: none; margin-top: 5px; }
  .headline { position: absolute; left: 520px; top: 36px; }
  .products {
    position: absolute; left: 500px; width: 700px; top: 252px;
    text-align: center; font-weight: 600; color: var(--teal); font-size: 24px; line-height: 36px;
  }
  .products .sep { color: var(--orange); font-weight: 400; margin: 0 6px; }
  .location {
    position: absolute; left: 500px; width: 700px; top: 348px;
    display: flex; justify-content: center; align-items: center; gap: 12px;
    font-size: 28px; color: var(--ink);
  }
  .bands { position: absolute; left: 0; bottom: 0; }
  .website, .phone {
    position: absolute; display: flex; align-items: center; color: var(--white);
  }
  .website { left: 16px; top: 444px; gap: 12px; font-size: 31px; }
  .phone { left: 560px; top: 420px; gap: 18px; font-size: 74px; font-weight: 600; letter-spacing: 1px; line-height: 1; }
</style>
</head>
<body>
<main class="billboard">
  <div class="brand">
    <span class="brand-square"></span>
    <span class="brand-name">PLANK<br>HAVEN</span>
  </div>

  <ul class="callouts">
    <li>
      <svg width="28" height="28" viewBox="0 0 28 28" aria-hidden="true"><rect x="2" y="4" width="22" height="22" rx="3" fill="none" stroke="var(--teal)" stroke-width="3"/><path d="M7 14l5 5 13-14" fill="none" stroke="var(--orange)" stroke-width="4" stroke-linecap="round" stroke-linejoin="round"/></svg>
      <span>Free Estimates</span>
    </li>
    <li>
      <svg width="28" height="28" viewBox="0 0 28 28" aria-hidden="true"><rect x="2" y="4" width="22" height="22" rx="3" fill="none" stroke="var(--teal)" stroke-width="3"/><path d="M7 14l5 5 13-14" fill="none" stroke="var(--orange)" stroke-width="4" stroke-linecap="round" stroke-linejoin="round"/></svg>
      <span>Wisconsin's In Stock<br>Flooring Store</span>
    </li>
  </ul>

  <svg class="headline" width="650" height="180" viewBox="0 0 650 180">
    <text x="42" y="76" font-family="Bebas Neue, sans-serif" font-size="94" fill="var(--teal)" textLength="568" lengthAdjust="spacingAndGlyphs">BIG CITY SELECTION</text>
    <text x="8" y="173" font-family="Bebas Neue, sans-serif" font-size="94" fill="var(--orange)" textLength="636" lengthAdjust="spacingAndGlyphs">SMALL TOWN SERVICE</text>
  </svg>

  <div class="products">
    Carpet<span class="sep">|</span>Hardwood<span class="sep">|</span>Laminate<br>
    Vinyl<span class="sep">|</span>Luxury Vinyl Plank<span class="sep">|</span>Window Treatments
  </div>

  <div class="location">
    <svg width="26" height="30" viewBox="0 0 26 30" aria-hidden="true"><path d="M13 2a9 9 0 0 0-9 9c0 7 9 15 9 15s9-8 9-15a9 9 0 0 0-9-9z" fill="none" stroke="var(--ink)" stroke-width="3"/><circle cx="13" cy="11" r="3.2" fill="var(--ink)"/><path d="M3 27h20" stroke="var(--ink)" stroke-width="3" stroke-linecap="round"/></svg>
    <span>Maple Falls, WI, Near Exit 114</span>
  </div>

  <svg class="bands" width="1200" height="104" viewBox="0 0 1200 104" aria-hidden="true">
    <polygon points="0,27 538,27 520,104 0,104" fill="var(--orange)"/>
    <polygon points="544,0 1200,0 1200,104 518,104" fill="var(--teal)"/>
    <polygon points="526,27 544,0 544,27" fill="var(--teal-dark)"/>
  </svg>

  <div class="website">
    <svg width="46" height="46" viewBox="0 0 46 46" aria-hidden="true"><circle cx="23" cy="23" r="22" fill="var(--white)"/><rect x="13" y="14" width="20" height="13" rx="1.5" fill="none" stroke="var(--orange)" stroke-width="2.6"/><path d="M10 31h26" stroke="var(--orange)" stroke-width="3" stroke-linecap="round"/></svg>
    <span>plankhavenstore.example</span>
  </div>

  <div class="phone">
    <svg width="64" height="64" viewBox="0 0 64 64" aria-hidden="true"><circle cx="32" cy="32" r="31" fill="var(--white)"/><path d="M22 17c2-1 4 0 5 2l3 6c1 2 0 3-1 4l-2 2c1 3 5 7 8 8l2-2c1-1 2-2 4-1l6 3c2 1 3 3 2 5-1 3-4 5-7 5-11-1-21-11-22-22 0-3 0-7 2-10z" fill="var(--teal)"/><path d="M36 20a9 9 0 0 1 8 8M36 13a16 16 0 0 1 15 15" fill="none" stroke="var(--teal)" stroke-width="3" stroke-linecap="round"/></svg>
    <span>715-381-6094</span>
  </div>
</main>
</body>
</html>
```